Hal's Remedies Business Card Design Project

I need a business card designed for my pharmacy Hal's Remedies. I would like just the logo on one side, maybe with black background and white lettering. The other side I would also like to include my logo which is attached. Also, please include my name and the following information:
Hal Norwick Owner/Pharm D.
Business address is 7163 N Birch Rd Sioux Falls, SD 57291.
Phone number is 605-318-6027 and fax # is 605-318-6031.
my email address is hal@halsremedies.example.
My website is www.halsremedies.example.
My business hours are Monday-Friday 8am-7 pm. Saturday 8am-12 pm. Sunday Closed.
I would like the design to include my logo colors, black, white, and neon green. Silver may be added as a highlight. Thanks.
Pharmacy
See above in product description

```html
<!DOCTYPE html>
<html lang="en">
<head>
<meta charset="utf-8">
<title>Hal's Remedies – Business Card</title>
<link rel="stylesheet" href="https://fonts.googleapis.com/css2?family=Open+Sans:wght@600;700;800&family=Lato:wght@400;700&display=swap">
<style>
  :root {
    --backdrop: #9a9a9a;
    --card-white: #ffffff;
    --ink: #1f1d1e;
    --ink-soft: #2e2c2d;
    --neon-green: #9ccc2e;
    --rule: #2a2a2a;
  }
  * { box-sizing: border-box; margin: 0; padding: 0; }
  html, body { width: 1200px; height: 900px; overflow: hidden; }
  body {
    background: var(--backdrop);
    font-family: "Lato", Arial, sans-serif;
    color: var(--ink);
    position: relative;
  }
  .card {
    position: absolute;
    left: 240px;
    width: 720px;
    height: 411px;
    background: var(--card-white);
    overflow: hidden;
    box-shadow: 0 6px 18px rgba(0,0,0,0.25);
  }
  .card--front { top: 26px; }
  .card--back  { top: 463px; }

  /* brand lockup */
  .brand {
    position: absolute;
    display: flex;
    align-items: center;
  }
  .brand__dot {
    width: 46px; height: 46px;
    border-radius: 50%;
    background: var(--neon-green);
  }
  .brand__divider {
    width: 2px; height: 86px;
    background: var(--rule);
    margin: 0 26px 0 40px;
  }
  .brand__name {
    font-family: "Open Sans", Arial, sans-serif;
    font-weight: 700;
    letter-spacing: -1.5px;
    color: var(--ink);
    white-space: nowrap;
  }

  /* front */
  .card--front .brand { left: 46px; top: 30px; }
  .card--front .brand__name { font-size: 50px; }
  .holder { position: absolute; left: 52px; top: 142px; }
  .holder__name {
    font-family: "Open Sans", Arial, sans-serif;
    font-weight: 700;
    font-size: 27px;
    letter-spacing: 2px;
  }
  .holder__title {
    font-size: 15px;
    font-weight: 700;
    letter-spacing: 1px;
    text-align: right;
    margin-top: 2px;
  }
  .contact {
    position: absolute; left: 40px; top: 232px;
    list-style: none;
    font-size: 14.5px;
    letter-spacing: 0.4px;
  }
  .contact__row { display: flex; gap: 22px; margin-bottom: 14px; }
  .contact__item { display: flex; align-items: center; gap: 8px; white-space: nowrap; }
  .contact__icon { width: 13px; height: 13px; flex: none; fill: var(--ink); }
  .card__band { position: absolute; inset: 0; width: 720px; height: 411px; }

  /* back */
  .card--back .brand { left: 70px; top: 52px; }
  .card--back .brand__dot { width: 58px; height: 58px; }
  .card--back .brand__divider { height: 110px; margin: 0 32px 0 48px; }
  .card--back .brand__name { font-size: 66px; }
  .hours {
    position: absolute; left: 70px; top: 240px; right: 60px;
    list-style: none;
    display: flex; justify-content: space-between;
    font-size: 15px; font-weight: 700; letter-spacing: 1px;
  }
  .hours__item { display: flex; align-items: center; gap: 10px; }
  .hours__item::before {
    content: ""; width: 10px; height: 10px; border-radius: 50%;
    background: var(--neon-green);
  }
</style>
</head>
<body>

<section class="card card--front" aria-label="Card front">
  <svg class="card__band" viewBox="0 0 720 411" aria-hidden="true">
    <polygon points="250,411 720,150 720,176 300,411" fill="var(--neon-green)"/>
    <polygon points="300,411 720,176 720,411" fill="var(--ink)"/>
  </svg>
  <div class="brand">
    <span class="brand__dot"></span>
    <span class="brand__divider"></span>
    <span class="brand__name">Hal's Remedies</span>
  </div>
  <div class="holder">
    <p class="holder__name">Hal Norwick</p>
    <p class="holder__title">Owner/Pharm D.</p>
  </div>
  <ul class="contact">
    <li class="contact__row">
      <span class="contact__item"><svg class="contact__icon" viewBox="0 0 16 16"><path d="M3 1l3 3-1.5 2a9 9 0 0 0 5.5 5.5L12 10l3 3-2 2C6 15 1 10 1 3z"/></svg>605-318-6027</span>
      <span class="contact__item"><svg class="contact__icon" viewBox="0 0 16 16"><path d="M4 1h6v4H4zM1 6h14v9H1zm3 3v2h8V9z"/></svg>605-318-6031</span>
    </li>
    <li class="contact__row">
      <span class="contact__item"><svg class="contact__icon" viewBox="0 0 16 16"><path d="M1 3h14v10H1zm1.5 1.5L8 9l5.5-4.5"/></svg>hal@halsremedies.example</span>
      <span class="contact__item"><svg class="contact__icon" viewBox="0 0 16 16"><path d="M8 1a7 7 0 1 0 0 14A7 7 0 0 0 8 1zm0 2a5 5 0 1 1 0 10A5 5 0 0 1 8 3z"/></svg>www.halsremedies.example</span>
    </li>
    <li class="contact__row">
      <span class="contact__item"><svg class="contact__icon" viewBox="0 0 16 16"><path d="M8 1a5 5 0 0 0-5 5c0 4 5 9 5 9s5-5 5-9a5 5 0 0 0-5-5zm0 3a2 2 0 1 1 0 4 2 2 0 0 1 0-4z"/></svg>7163 N Birch Rd, Sioux Falls, SD 57291</span>
    </li>
  </ul>
</section>

<section class="card card--back" aria-label="Card back">
  <div class="brand">
    <span class="brand__dot"></span>
    <span class="brand__divider"></span>
    <span class="brand__name">Hal's Remedies</span>
  </div>
  <ul class="hours">
    <li class="hours__item">Monday-Friday 8am-7pm</li>
    <li class="hours__item">Saturday 8am-12pm</li>
    <li class="hours__item">Sunday Closed</li>
  </ul>
</section>

</body>
</html>
```